My dad's 70th birthday party invite - Greek theme!

My dad isn't actually Greek, but his party will be at a Greek restaurant, so we thought it'd be a fun to have a Greek theme for the invitation to his 70th birthday party.

The invite will be sent out by email, so it needs to look good on screen, AND when it's printed out by the recipients, likely onto A4 paper and put up on a noticeboard/stuck to the fridge as a reminder etc.
Updates

Reason: A designer has asked us to extend the deadline and as we're not in a rush to complete this particular project, we've done so. Thanks everyone for their designs to date.

Target Market(s)

my dad's friends and family - average 50-70years old

Industry/Entity Type

Restaurant

Requirements
Must have
• For: Lanton's 70th birthday
Date: 30 Nov 2013
Time: 7.30pm
Place: Zorvik Taverna, 48 Wrenmoorly Road, Tulsa Vin

RSVP by: Friday 1 November
to: kel@qpx.com.au
(Please also let us know of any specific dietary requirements eg vegetarian, seafood allergy etc. Thanks. And please, no presents - just really hoping you can join us on the night!)
Nice to have
• Some ideas for you:
- he loves the blue & white of Greece eg white buildings against blue ocean, Greek flag etc
- and red geraniums/pink bouganvillea - quintessential (yet stylish!) Greece
- also, maybe you could use the names of the dishes we'll be having for dinner somehow? ie:
MEZES
Taramosalata
Tzatziki
Skordalia
Hommus
Haloumi
Psití Melitzána
Pita
Eliés
Dolmathes
THALASINA
Chtapódi Psitó
KalamáriaTiganitá
KREATA
Souvlaki
Arní
Lachaniká se Sáltsa - Mumbaldi
SALATA
Baklava
Paximádi Rolá
Kataifi
Kourabiethes
Greek Coffee

Hope that helps!
Should not have
• We'd prefer a simple colour scheme, ie not too many different colours.

```html
<!DOCTYPE html>
<html lang="en">
<head>
<meta charset="utf-8">
<title>Lanton's 70th – Invitation</title>
<link rel="stylesheet" href="https://fonts.googleapis.com/css2?family=Cinzel:wght@400;700;900&family=Cinzel+Decorative:wght@700;900&family=Alegreya+SC:wght@500;700&family=Orbitron:wght@700;900&display=swap">
<style>
  :root {
    --sky: #5fc6ef;
    --aegean: #10a9e6;
    --pale: #c9e8f7;
    --pale-soft: #dcf0fa;
    --white: #ffffff;
  }
  * { box-sizing: border-box; margin: 0; padding: 0; }
  html, body { width: 849px; height: 1200px; overflow: hidden; background: var(--white); }
  .invite {
    position: relative; width: 849px; height: 1200px; overflow: hidden;
    background: var(--pale);
    font-family: "Alegreya SC", serif;
  }
  .hero {
    position: absolute; left: 0; top: 0; width: 849px; height: 800px;
    background: linear-gradient(180deg, var(--sky) 0%, #86d3f3 45%, #a6ddf5 100%);
  }
  .temple {
    position: absolute; left: 28px; top: 10px; width: 793px; height: 770px;
    background: linear-gradient(180deg, rgba(255,255,255,0.18) 0%, rgba(255,255,255,0.32) 60%, rgba(255,255,255,0.45) 100%);
  }
  .stripe { position: absolute; height: 40px; width: 218px; background: var(--aegean); }
  .stripe.left { left: 28px; }
  .stripe.right { left: 601px; }
  .divider {
    position: absolute; left: 0; top: 800px; width: 849px; height: 12px;
    background: var(--white); opacity: 0.85;
  }
  .title-band {
    position: absolute; left: 14px; top: 78px; width: 819px; height: 93px;
    background: var(--aegean);
  }
  .title {
    position: absolute; left: 0; top: 66px; width: 849px; text-align: center;
    font-family: "Cinzel", serif; font-weight: 700; font-size: 104px;
    color: var(--white); letter-spacing: 1px; line-height: 1.1;
  }
  .guest {
    position: absolute; left: 0; top: 325px; width: 849px; text-align: center;
    font-family: "Cinzel Decorative", serif; font-weight: 900; font-size: 52px;
    color: var(--aegean);
  }
  .age {
    position: absolute; left: 288px; top: 370px;
    font-family: "Cinzel", serif; font-weight: 900; font-size: 170px;
    color: var(--white); line-height: 1;
  }
  .age sup {
    font-size: 54px; vertical-align: 0; position: relative; top: -84px; left: 4px;
  }
  .slot { position: absolute; top: 525px; width: 118px; text-align: center; }
  .slot.date { left: 265px; }
  .slot.time { left: 465px; }
  .slot-label {
    font-family: "Cinzel", serif; font-weight: 700; font-size: 36px;
    color: var(--aegean); line-height: 1;
  }
  .slot-box { margin-top: 6px; height: 92px; background: var(--aegean); padding: 7px 7px 0; }
  .slot-figure {
    height: 44px; border: 4px solid var(--white); background: var(--aegean);
    font-family: "Orbitron", sans-serif; font-weight: 900; font-size: 36px;
    color: var(--white); line-height: 36px;
  }
  .slot-note {
    margin-top: 8px; font-family: "Orbitron", sans-serif; font-weight: 700;
    font-size: 16px; color: var(--white); letter-spacing: 1px;
  }
  .venue {
    position: absolute; left: 0; top: 718px; width: 849px; text-align: center;
    color: var(--aegean);
  }
  .venue-name {
    font-family: "Cinzel", serif; font-weight: 700; font-size: 37px; line-height: 1.1;
  }
  .venue-address {
    margin-top: 4px;
    font-family: "Cinzel", serif; font-weight: 700; font-size: 19px; letter-spacing: 1px;
  }
  .heading {
    position: absolute; text-align: center;
    font-family: "Cinzel", serif; font-weight: 700; font-size: 34px;
    color: var(--aegean); line-height: 1;
  }
  .heading.rsvp { left: 26px; width: 365px; top: 848px; }
  .heading.important { left: 26px; width: 365px; top: 993px; }
  .heading.menu { left: 460px; width: 389px; top: 848px; }
  .panel {
    position: absolute; left: 26px; width: 365px;
    border: 6px solid var(--aegean); background: var(--pale-soft);
  }
  .panel::after {
    content: ""; position: absolute; inset: 4px; border: 2px solid var(--white);
    pointer-events: none;
  }
  .panel.rsvp-panel { top: 893px; height: 90px; padding: 16px 14px; }
  .panel.notes-panel { top: 1028px; height: 161px; padding: 12px 16px; }
  .rsvp-line {
    font-family: "Cinzel", serif; font-weight: 700; font-size: 17px;
    color: var(--aegean); line-height: 1.55;
  }
  .notes { font-size: 19px; font-weight: 500; color: var(--aegean); line-height: 1.08; }
  .menu-list {
    position: absolute; left: 460px; top: 893px; width: 389px; list-style: none;
  }
  .menu-row {
    display: grid; grid-template-columns: 1fr 1fr; height: 21px; margin-bottom: 4.6px;
    align-items: center; padding-left: 22px;
    background: var(--aegean);
    font-family: "Cinzel", serif; font-weight: 900; font-size: 13px;
    color: var(--white); letter-spacing: 0.3px; white-space: nowrap;
  }
  .menu-row.last { background: transparent; color: var(--aegean); }
</style>
</head>
<body>
<main class="invite">
  <section class="hero">
    <div class="temple" role="img" aria-label="Pale Greek temple with pediment, fluted columns and broad steps"></div>
    <div class="stripe left" style="top:353px"></div>
    <div class="stripe left" style="top:439px"></div>
    <div class="stripe left" style="top:524px"></div>
    <div class="stripe left" style="top:610px"></div>
    <div class="stripe right" style="top:353px"></div>
    <div class="stripe right" style="top:439px"></div>
    <div class="stripe right" style="top:524px"></div>
    <div class="stripe right" style="top:610px"></div>

    <div class="title-band"></div>
    <h1 class="title">INVITATION</h1>

    <p class="guest">Lanton's</p>
    <p class="age">70<sup>TH</sup></p>

    <div class="slot date">
      <div class="slot-label">DATE</div>
      <div class="slot-box">
        <div class="slot-figure">30</div>
        <div class="slot-note">NOV 2013</div>
      </div>
    </div>
    <div class="slot time">
      <div class="slot-label">TIME</div>
      <div class="slot-box">
        <div class="slot-figure">730</div>
        <div class="slot-note">P M</div>
      </div>
    </div>

    <div class="venue">
      <p class="venue-name">ZORVIK TAVERNA</p>
      <p class="venue-address">48 WRENMOORLY ROAD, TULSA VIN</p>
    </div>
  </section>
  <div class="divider"></div>

  <h2 class="heading rsvp">RSVP</h2>
  <div class="panel rsvp-panel">
    <p class="rsvp-line">RSVP BY: FRIDAY 1 NOVEMBER</p>
    <p class="rsvp-line">TO: KEL@QPX.COM.AU</p>
  </div>

  <h2 class="heading important">IMPORTANT</h2>
  <div class="panel notes-panel">
    <p class="notes">Please also let us know of any specific dietary requirements eg vegetarian, seafood allergy etc. Thanks. And please, no presents - just really hoping you can join us on the night!)</p>
  </div>

  <h2 class="heading menu">THE MENU</h2>
  <ul class="menu-list">
    <li class="menu-row"><span>MEZES</span><span>TARAMOSALATA</span></li>
    <li class="menu-row"><span>TZATZIKI</span><span>SKORDALIA</span></li>
    <li class="menu-row"><span>HOMMUS</span><span>HALOUMI</span></li>
    <li class="menu-row"><span>PSITÍ MELITZÁNA</span><span>PITA</span></li>
    <li class="menu-row"><span>DOLMATHES</span><span>THALASINA</span></li>
    <li class="menu-row"><span>KALAMÁRIATIGANITÁ</span><span>KREATA</span></li>
    <li class="menu-row"><span>ARNÍ LACHANIKÁ SE</span><span>SÁLTSA - MUMBALDI</span></li>
    <li class="menu-row"><span>BAKLAVA</span><span>PAXIMÁDI ROLÁ</span></li>
    <li class="menu-row"><span>KOURABIETHES</span><span>GREEK COFFEE</span></li>
    <li class="menu-row"><span>SOUVLAKI</span><span>SALATA</span></li>
    <li class="menu-row"><span>KATAIFI</span><span>CHTAPÓDI PSITÓ</span></li>
    <li class="menu-row last"><span>ELIÉS</span><span></span></li>
  </ul>
</main>
</body>
</html>
```